Tequila Velmoras Web Design Project

We are launching a new Ultra Premium Tequila; the brand name is "Velmoras".
Velmoras was the colloquial name given to Spanish immigrants that came to America in the 19th and early part of the 20th centuries, made fortune and went back to Spain to propel even greater opportunities for those in their homeland, started banks, built schools, roads, built eclectic houses, some acquired noble titles, they were brazen, altruist and built a better world along the way.
Our product is 100% Blue Agave and will have the 4 types of tequila: Silver, Reposado, Añejo and Extra Añejo.
Updates

Dear All,
I have attached some more information/content for your review.
Kind Regards,

After some consideration, we have decided to include our line of Premium Margaritas on the same site.
Our Margaritas are made with 100% Blue Agave Silver Tequila and lightly sweetened with Agave Nectar.
Please see file with the 5 different flavors available.
Thank you,

Target Market(s)

Our target market is affluent people, especially Hispanics, because most of the have a Spanish heritage and/or ancestry; also, entrepreneurs of today.

Industry/Entity Type

Product

Requirements
Must have
• We will provide pictures and content/text for the pages.

```html
<!DOCTYPE html>
<html lang="en">
<head>
<meta charset="utf-8">
<title>Tequila Velmoras</title>
<link rel="stylesheet" href="https://fonts.googleapis.com/css2?family=Rokkitt:wght@400;500&family=Source+Sans+3:wght@400;600&display=swap">
<style>
:root{
  --bg-dark:#2e2929;
  --bg-mid:#3d3737;
  --bg-glow:#5a5353;
  --band-light:#f6ebc9;
  --band-deep:#e6d19c;
  --ink:#2a2220;
  --brown:#8a3a1c;
  --text:#575352;
  --panel:#f4f4f4;
  --panel-edge:#e9e9e9;
  --rule:#c9c9c9;
  --muted:#8f8884;
  --light:#e9e2d8;
  --amber-1:#e9a948;
  --amber-2:#c98428;
  --field-1:#7e8a6e;
  --field-2:#3f4a36;
  --field-3:#2a2a22;
}
*{margin:0;padding:0;box-sizing:border-box}
html,body{width:1200px;height:1041px;overflow:hidden;background:var(--bg-dark)}
.page{
  position:relative;width:1150px;height:998px;
  transform:scale(1.04348);transform-origin:0 0;
  background:
    radial-gradient(ellipse 420px 520px at 260px 420px,var(--bg-glow),transparent 70%),
    linear-gradient(var(--bg-mid),var(--bg-dark));
  font-family:"Source Sans 3",sans-serif;color:var(--text);
}
.topbar{position:absolute;left:0;top:0;width:1150px;height:68px;background:linear-gradient(#3a3434,#231f1f);border-top:3px solid #4a4444}
.phone{position:absolute;left:152px;top:24px;font:400 21px "Rokkitt",serif;color:var(--light);letter-spacing:.3px}
.search{position:absolute;left:798px;top:23px;width:170px;height:24px;background:#fff;border-radius:2px;font:italic 11px "Source Sans 3",sans-serif;color:#aaa;padding:6px 14px}
.search svg{position:absolute;right:14px;top:6px}
.nav{position:absolute;left:0;top:68px;width:1150px;height:58px;background:linear-gradient(90deg,#b9a77a,var(--band-light) 8%,var(--band-deep) 50%,var(--band-light) 92%,#b9a77a);box-shadow:0 3px 6px rgba(0,0,0,.35)}
.nav a{position:absolute;top:19px;font:400 17px "Rokkitt",serif;color:var(--ink);text-decoration:none}
.nav a.active{color:var(--brown);border-bottom:1px solid var(--brown)}
.nav .sep{position:absolute;top:15px;width:1px;height:30px;background:#c9b888;box-shadow:1px 0 0 #fff6dc}
.brand{position:absolute;left:435px;top:72px;width:280px;text-align:center;font:500 40px "Rokkitt",serif;color:var(--ink);letter-spacing:2px}
.connect{position:absolute;left:796px;top:157px;font-size:13px;color:var(--muted)}
.social{position:absolute;top:149px;width:32px;height:32px;border-radius:50%;background:#6d6663}
.panel{position:absolute;left:360px;top:206px;width:698px;height:724px;border-radius:14px;background:linear-gradient(var(--panel),#f9f9f9 60%,var(--panel-edge))}
.bottle-photo{position:absolute;left:122px;top:192px;width:344px;height:746px;border-radius:18px;
  background:linear-gradient(180deg,#2a2626 0%,#2a2626 20%,var(--amber-2) 21%,var(--amber-1) 60%,var(--amber-2) 86%,#d9d6d0 100%)}
.hero{position:absolute;left:433px;top:220px;width:615px;height:207px;border-radius:12px;overflow:hidden;
  background:linear-gradient(180deg,#c9c6b8 0%,#8f9a80 22%,var(--field-1) 30%,var(--field-2) 65%,var(--field-3) 100%)}
.hero-title{position:absolute;right:26px;top:112px;font:500 28px "Rokkitt",serif;color:#fff;text-shadow:0 1px 3px rgba(0,0,0,.6)}
h2{font:400 19px "Rokkitt",serif;color:var(--brown)}
.welcome{position:absolute;left:477px;top:451px;width:574px}
.welcome p{margin-top:14px;font-size:12.5px;line-height:22.2px;color:var(--text);hyphens:manual}
.rule{position:absolute;height:1px;background:var(--rule)}
.vrule{position:absolute;width:1px;background:var(--rule)}
.crest{position:absolute;left:738px;top:591px;width:28px;height:28px;border-radius:50%;border:2px solid #b9b9b9;background:#e4e4e4}
.block{position:absolute}
.block h2{font-size:17.5px}
.list{list-style:none;display:grid;grid-template-columns:113px 120px;row-gap:9px;margin-top:19px;font-size:13px;color:#3b3838}
.list li{padding-left:16px;position:relative;line-height:18px}
.list li::before{content:"";position:absolute;left:1px;top:6px;width:6px;height:6px;border-radius:50%;background:#3b3838}
.list a{color:var(--brown)}
.more{display:block;margin:12px 0 0 17px;font-size:13px;color:var(--brown)}
.news{list-style:none;margin-top:18px;font-size:12.5px;line-height:20px;color:#3b3838;width:240px}
.news li{position:relative;padding-left:16px;margin-bottom:11px}
.news li::before{content:"";position:absolute;left:1px;top:7px;width:6px;height:6px;border-radius:50%;background:#3b3838}
.footer{position:absolute;left:568px;top:957px;font-size:12.5px;color:#c4bdb8}
</style>
</head>
<body>
<div class="page">
  <header class="topbar">
    <div class="phone">Call us : 555 014 2368</div>
    <div class="search">Search
      <svg width="11" height="11" viewBox="0 0 11 11"><circle cx="4.5" cy="4.5" r="3.3" fill="none" stroke="#bbb" stroke-width="1.3"/><path d="M7 7l3 3" stroke="#bbb" stroke-width="1.5"/></svg>
    </div>
  </header>

  <nav class="nav">
    <a class="active" style="left:118px" href="#">Home</a>
    <span class="sep" style="left:177px"></span>
    <a style="left:196px" href="#">Our Collection</a>
    <span class="sep" style="left:316px"></span>
    <a style="left:335px" href="#">Our Legacy</a>
    <a style="left:743px" href="#">News</a>
    <span class="sep" style="left:799px"></span>
    <a style="left:815px" href="#">Events</a>
    <span class="sep" style="left:877px"></span>
    <a style="left:894px" href="#">Contact us</a>
  </nav>
  <div class="brand">VELMORAS</div>

  <div class="connect">Connect with us :</div>
  <span class="social" style="left:903px" role="img" aria-label="Social network link"></span>
  <span class="social" style="left:949px" role="img" aria-label="Social network link"></span>
  <span class="social" style="left:994px" role="img" aria-label="News feed link"></span>

  <main>
    <div class="panel"></div>

    <div class="bottle-photo" role="img" aria-label="Product photograph of a Velmoras Extra Añejo tequila bottle"></div>

    <section class="hero" role="img" aria-label="Photograph of a worker harvesting blue agave in a field">
      <div class="hero-title">Pure and Simple</div>
    </section>

    <section class="welcome">
      <h2>Welcome to Velmoras</h2>
      <p>Sed ut perspiciatis unde omnis iste natus error sit voluptatem accusantium doloremque laudantium, totam rem aperiam, eaque ipsa quae ab illo inventore veritatis et quasi architecto beatae vitae dicta sunt expli&shy;cabo. Nemo enim ipsam voluptatem quia voluptas sit aspernatur aut odit aut fugit, sed quia consequuntur magni dolores eos qui ratione voluptatem sequi nesciunt.</p>
    </section>

    <div class="rule" style="left:477px;top:605px;width:253px"></div>
    <div class="rule" style="left:773px;top:605px;width:273px"></div>
    <div class="crest"></div>

    <section class="block" style="left:477px;top:638px">
      <h2>Our Tequila Collection</h2>
      <ul class="list">
        <li><a href="#">Silver</a></li><li>Añejo</li>
        <li>Reposado</li><li>Extra Añejo</li>
      </ul>
    </section>
    <div class="vrule" style="left:752px;top:645px;height:103px"></div>
    <section class="block" style="left:808px;top:638px">
      <h2>Our Margaritas Collection:</h2>
      <ul class="list">
        <li>Classic Lime</li><li>Mango</li>
        <li>Strawberry</li><li>Grapefruit</li>
        <li>Blueberry</li>
      </ul>
    </section>

    <div class="rule" style="left:479px;top:768px;width:246px"></div>
    <div class="rule" style="left:777px;top:768px;width:269px"></div>

    <section class="block" style="left:477px;top:785px">
      <h2>Our Legacy</h2>
      <ul class="list">
        <li>Jima</li><li>Aging</li>
        <li>Process</li><li>Bottling text</li>
      </ul>
      <a class="more" href="#">Include the Selection</a>
    </section>
    <div class="vrule" style="left:752px;top:790px;height:107px"></div>
    <section class="block" style="left:808px;top:785px">
      <h2>News and Events</h2>
      <ul class="news">
        <li>Sed ut perspiciatis unde omnis iste natus error sit voluptatem accusantium</li>
        <li>Sed ut perspiciatis unde omnis iste natus error sit voluptatem accusantium</li>
      </ul>
    </section>
  </main>

  <footer class="footer">Copyright © 2012 www.velmoras.com&nbsp; All rights reserved.</footer>
</div>
</body>
</html>
```